K7R Business Cards

Business Cards

Contact Information for Business Card

Company name, owner name, license #s, phone & email

Requirements
Should not have
• mailing address

```html
<!DOCTYPE html>
<html lang="en">
<head>
<meta charset="utf-8">
<title>K7R Business Cards</title>
<link rel="stylesheet" href="https://fonts.googleapis.com/css2?family=Arimo:wght@400;700&display=swap">
<style>
  :root {
    --backdrop: #3b3b3b;
    --card: #ffffff;
    --brand-blue: #1b3a9c;
    --accent-red: #c8161d;
    --ink: #1a1a1a;
    --divider: #c9c9c9;
  }
  * { box-sizing: border-box; margin: 0; padding: 0; }
  html, body { width: 1200px; height: 689px; overflow: hidden; }
  body {
    background: var(--backdrop);
    font-family: "Arimo", Arial, sans-serif;
    display: flex;
    align-items: center;
    justify-content: center;
    gap: 60px;
  }
  .card {
    width: 520px;
    height: 300px;
    background: var(--card);
    border-radius: 22px;
    position: relative;
    overflow: hidden;
  }
  .card--front {
    display: flex;
    align-items: center;
    justify-content: center;
  }
  .wordmark {
    color: var(--brand-blue);
    font-weight: 700;
    font-size: 42px;
    letter-spacing: 1px;
    white-space: nowrap;
  }
  .card--back {
    display: flex;
    align-items: center;
  }
  .card--back .brand {
    width: 290px;
    flex: none;
    display: flex;
    align-items: center;
    justify-content: center;
    padding: 60px 20px 0;
  }
  .card--back .wordmark { font-size: 21px; letter-spacing: 0.5px; }
  .divider {
    width: 1px;
    height: 180px;
    flex: none;
    background: var(--divider);
  }
  .contact {
    padding-left: 26px;
    color: var(--ink);
    font-size: 13px;
    line-height: 1.4;
  }
  .contact__name {
    color: var(--brand-blue);
    font-weight: 700;
    font-size: 22px;
    line-height: 1.1;
  }
  .contact__role { font-size: 12px; margin-bottom: 18px; }
  .contact__line { display: flex; align-items: center; gap: 7px; }
  .contact__line svg { width: 11px; height: 11px; flex: none; }
</style>
</head>
<body>
  <section class="card card--front">
    <span class="wordmark">K7R CONSTRUCTION</span>
  </section>

  <section class="card card--back">
    <div class="brand">
      <span class="wordmark">K7R CONSTRUCTION</span>
    </div>
    <div class="divider"></div>
    <div class="contact">
      <p class="contact__name">Dana Whitfield</p>
      <p class="contact__role">President</p>
      <p class="contact__line">
        <svg viewBox="0 0 12 12" aria-hidden="true"><path fill="var(--accent-red)" d="M3 1l2 2.4-1.2 1.3c.7 1.5 1.9 2.7 3.4 3.4L8.6 7 11 9l-1 1.8C5.2 11 1 6.8 1.2 2z"/></svg>
        555-201-4476
      </p>
      <p class="contact__line">
        <svg viewBox="0 0 12 12" aria-hidden="true"><rect x="0.5" y="2" width="11" height="8" fill="var(--accent-red)"/><path d="M0.5 2L6 6.5 11.5 2" fill="none" stroke="#fff" stroke-width="1"/></svg>
        dwhitfield@mailbox.com
      </p>
      <p class="contact__license">MN License #BC482615</p>
    </div>
  </section>
</body>
</html>
```